Vimbalo Food Cafeteria and Food Services

I´m a Mexican Company , I dont know if we can built a US web page, but what we are a Cafeteria and Food Services, basically for industry , we produce food at companies for their employes, I have a Brochure to share if you consider. Our logo was made by your team. We need to have a Web page for our potentials custumers find us easy by internet

Target Market(s)

Food for manufacturers /Industry

Industry/Entity Type

Manufacturer

Number of Pages Required

4 page

Font styles to use
Sans Serif

Requirements
Must have
• Great images, Spanish and English options, our mision , vision , our actual customers , (be able to remove it also), our Certifications, our actual packages for services, our 90 days menu, our catering services, Contact page , Cafeteria Services , our meals serve now .
Nice to have
• Great pics, easy to access , and easy to move into the web page, nutricional ideas.
Should not have
• Fluorescent Color , or brilliant

```html
<!DOCTYPE html>
<html lang="en">
<head>
<meta charset="utf-8">
<title>Vimbalo – Cafeteria and Food Services</title>
<link href="https://fonts.googleapis.com/css2?family=Mulish:wght@400;600;700;800;900&display=swap" rel="stylesheet">
<style>
  :root{
    --maroon:#3d1113;
    --orange:#cf6a32;
    --green:#1b8a45;
    --headline:#138a45;
    --light-green:#8cc152;
    --white:#ffffff;
    --text:#2a1a1a;
    --photo-a:#e9ece4;
    --photo-b:#b7c58a;
    --photo-c:#d9b98a;
  }
  *{margin:0;padding:0;box-sizing:border-box}
  html,body{width:1200px;height:703px;overflow:hidden;background:var(--white)}
  body{font-family:"Mulish",Arial,sans-serif;color:var(--text)}
  .canvas{position:relative;width:1200px;height:703px;overflow:hidden}
  .hero-photo{position:absolute;inset:0;
    background:
      radial-gradient(ellipse 380px 300px at 1000px 260px, #c9d28f 0%, rgba(201,210,143,0) 70%),
      radial-gradient(ellipse 420px 260px at 900px 600px, var(--photo-c) 0%, rgba(217,185,138,0) 75%),
      radial-gradient(ellipse 260px 200px at 780px 420px, #7a9a4a 0%, rgba(122,154,74,0) 70%),
      linear-gradient(120deg, var(--photo-a) 0%, #dfe3d8 40%, var(--photo-b) 70%, var(--photo-c) 100%);}
  .side-shapes{position:absolute;left:0;top:0}
  .flags{position:absolute;left:14px;top:6px;display:flex;gap:10px}
  .flag{width:20px;height:13px;display:flex}
  .flag-mx span{flex:1}
  .flag-us{background:repeating-linear-gradient(#b22234 0 1.9px,#fff 1.9px 3.7px);position:relative}
  .flag-us::before{content:"";position:absolute;left:0;top:0;width:9px;height:7px;background:#3c3b6e}
  .brand{position:absolute;left:14px;top:50px;width:180px;text-align:center}
  .brand-dot{width:60px;height:60px;border-radius:50%;background:var(--green);margin:0 auto 14px}
  .brand-name{font-size:33px;font-weight:900;color:var(--maroon);line-height:1;letter-spacing:.5px}
  .brand-tag{font-size:11px;font-weight:700;color:var(--maroon);margin-top:6px}
  .phone{position:absolute;left:13px;top:212px;display:flex;align-items:center;gap:8px;color:var(--white);font-weight:800;font-size:17px}
  .nav{position:absolute;left:14px;top:284px;list-style:none}
  .nav li{font-size:12px;font-weight:700;color:var(--white);height:23px;display:flex;align-items:center;gap:6px;text-transform:uppercase}
  .nav li.active{color:var(--maroon)}
  .nav li::before{content:"";width:5px;height:5px;border-radius:50%;background:currentColor;margin-right:4px}
  .nav li.sub{padding-left:35px;font-size:11.5px}
  .nav li.sub::before{display:none}
  .nav li.gap{margin-top:7px}
  .social{position:absolute;left:13px;top:526px;width:106px;height:32px;border-top:1px solid var(--maroon);border-bottom:1px solid var(--maroon);display:flex;align-items:center;gap:10px;padding-left:9px}
  .social span{width:11px;height:11px;border-radius:50%;background:var(--white)}
  .ring{position:absolute;left:184px;top:248px;width:422px;height:422px;border-radius:50%;background:rgba(255,255,255,.45)}
  .panel{position:absolute;left:197px;top:261px;width:396px;height:396px;border-radius:50%;background:var(--white);text-align:center;padding:85px 30px 0}
  .headline{font-size:24px;font-weight:900;color:var(--headline);letter-spacing:.3px}
  .intro{font-size:13.4px;line-height:18.5px;margin-top:6px;color:var(--text)}
  .btn{display:inline-block;margin-top:18px;width:145px;height:36px;border:2px solid var(--maroon);border-radius:3px;font-size:12px;font-weight:800;color:var(--maroon);line-height:32px;text-transform:uppercase}
  .dots{position:absolute;left:0;right:0;top:368px;display:flex;justify-content:center;gap:5px}
  .dots span{width:9px;height:9px;border-radius:50%;border:1px solid var(--light-green)}
  .dots span.on{background:var(--light-green)}
  .copyright{position:absolute;right:13px;bottom:12px;font-size:9px;font-weight:700;color:var(--maroon)}
</style>
</head>
<body>
<div class="canvas">
  <div class="hero-photo" role="img" aria-label="Close-up photo of a fresh taco salad bowl with avocado, tomato and cheese"></div>

  <svg class="side-shapes" width="1200" height="703" viewBox="0 0 1200 703" aria-hidden="true">
    <path d="M0 0 H130 L160 26 H0 Z" fill="var(--maroon)"/>
    <path d="M0 26 H160 C198 70 214 140 211 207 H0 Z" fill="var(--white)"/>
    <path d="M0 207 H211 C209 220 208 232 206 243 H0 Z" fill="var(--green)"/>
    <path d="M0 243 H206 C190 420 172 560 178 703 H0 Z" fill="var(--orange)"/>
  </svg>

  <div class="flags">
    <div class="flag flag-mx"><span style="background:#006847"></span><span style="background:#fff"></span><span style="background:#ce1126"></span></div>
    <div class="flag flag-us"></div>
  </div>

  <div class="brand">
    <div class="brand-dot"></div>
    <div class="brand-name">Vimbalo</div>
    <div class="brand-tag">Cafeteria and Food Services</div>
  </div>

  <div class="phone">
    <svg width="26" height="26" viewBox="0 0 26 26" aria-hidden="true">
      <circle cx="13" cy="13" r="11.5" fill="none" stroke="#fff" stroke-width="2"/>
      <path d="M9 7 l2.5 3 -1.4 1.6 c1 2 2.3 3.3 4.3 4.3 l1.6-1.4 3 2.5 -1.6 2 c-4.8-.4-9.4-5-9.8-9.8z" fill="#fff"/>
    </svg>
    555.010.0199
  </div>

  <ul class="nav">
    <li class="active">Home</li>
    <li>About Us</li>
    <li>Services</li>
    <li class="sub">Catering</li>
    <li class="sub">Cafeteria</li>
    <li class="gap">Packages</li>
    <li>Gallery</li>
    <li>Clients</li>
    <li>Contact</li>
  </ul>

  <div class="social" aria-label="Social links"><span></span><span></span><span></span><span></span></div>

  <div class="ring"></div>
  <div class="panel">
    <h1 class="headline">HEADLINE GOES HERE</h1>
    <p class="intro">Lorem ipsum dolor sit amet, consectetur adipiscing elit. Aliquam commodo tortor augue. In lobortis sapien sit amet euismod commodo. Aenean nec tempor odio, vel gravida ipsum. Proin tempor vitae felis ac pulvinar. Quisque facilisis condimentum massa, vel ultrices nisl tempor at. Sed fringilla felis arcu, quis aliquet ipsum hendrerit tincidunt. Mauris facilisis ante velit pulvinar.</p>
    <span class="btn">&gt; Learn More</span>
    <div class="dots"><span class="on"></span><span></span><span></span><span></span></div>
  </div>

  <div class="copyright">©2017 Vimbalo Food Cafeteria and Food Services.</div>
</div>
</body>
</html>
```